Email Template for AI Website Builder Marketing Campaign

Update: All the designs submitted have too much content for an email template. I have attached a mockup example of a simplified design. Please follow this guideline to revise your design to be less "wordy" and have less content to optimize the delivery rate of the emails. I have also attached the images I used to create the mockup. Feel free to use these images for your revised designs.
Original Brief:
I need a catchy email template for my new AI Website Builder, WebQuilt.ai. The template must be professional, colorful, yet not too complex. The concept of the product is this:
WebQuilt uses Artificial Intelligence (AI) to instantly build stunning websites, absolutely FREE. The user simply specifies their business name and business category (industry), and their stunning new website appears before their eyes!
The template will be used in MailChimp, so please provide the code that I can simply paste into the email body.
Here is a screenshot of our new website (which is not online yet) so you can match the color scheme and style of the email template to the new website design:
https://pixbinstore.com/art_img/7310582/2208634/48165027/9qrt41hwk826zlmpb3nqd7wyex_image.jpg
Let me know if you have any questions.
Thanks!
All submitted designs are too lengthy (too much content) for an email template. I will provide a mockup showing a sample of how you can simplify your design to function better as an email template and better suit my needs. I appreciate your patience!

```html
<!DOCTYPE html>
<html lang="en">
<head>
<meta charset="utf-8">
<title>WebQuilt – AI Website Builder</title>
<link href="https://fonts.googleapis.com/css2?family=Poppins:wght@300;400;500;600;700&display=swap" rel="stylesheet">
<style>
:root{
  --navy:#0b1230;
  --navy-footer:#1b2c58;
  --hero-a:#0c1638;
  --hero-b:#1b3f8f;
  --cyan:#1ea7e4;
  --blue:#1a86e0;
  --blue-deep:#0f2a6b;
  --ring:#8fc6f2;
  --pale:#eaf3fd;
  --ink:#111a33;
  --muted:#3c4560;
  --name:#1f5aa8;
  --star:#f5b400;
  --quote:#e4e7ee;
  --white:#ffffff;
}
*{margin:0;padding:0;box-sizing:border-box}
html,body{width:1200px;height:3462px;overflow:hidden;background:var(--white)}
body{font-family:'Poppins',sans-serif;color:var(--ink);position:relative}
.abs{position:absolute}

.header{left:0;top:0;width:1200px;height:120px;background:var(--navy)}
.brand{display:flex;align-items:center;gap:18px;color:var(--white);font-weight:600;font-size:54px;line-height:1}
.brand-mark{width:56px;height:56px;border-radius:50%;background:var(--cyan)}
.header .brand{left:46px;top:32px}
.social{right:46px;top:41px;display:flex;gap:22px}
.social span{width:40px;height:40px;border-radius:50%;background:#1a4fa8}

.hero{left:0;top:120px;width:1200px;height:687px;background:linear-gradient(120deg,var(--hero-a) 0%,#10205a 55%,var(--hero-b) 100%)}
.hero-art{left:498px;top:0;width:702px;height:687px;background:radial-gradient(ellipse at 55% 50%,#2f7fe0 0%,#173a8c 45%,rgba(16,32,90,0) 75%)}
.hero-copy{left:46px;top:100px;color:var(--white);font-size:52px;line-height:58px;font-weight:400}
.hero-copy b{font-weight:700}
.hero-copy .free{color:var(--cyan);font-weight:700}
.btn{left:50px;top:526px;width:310px;height:57px;background:var(--cyan);color:var(--white);font-size:27px;font-weight:500;display:flex;align-items:center;justify-content:center;border-radius:3px}

.eyebrow{left:0;width:1200px;top:892px;text-align:center;color:var(--blue);font-size:29px}
.title{left:0;width:1200px;text-align:center;font-size:45px;font-weight:400;color:var(--ink)}
.title b{font-weight:700}
.step-line{top:1168px;height:0;border-top:3px dashed var(--blue)}
.step{width:284px;height:284px;border-radius:50%;background:var(--ring);top:1027px;display:flex;align-items:center;justify-content:center}
.step .core{width:244px;height:244px;border-radius:50%;background:var(--blue);display:flex;align-items:center;justify-content:center}
.step-label{width:320px;top:1334px;text-align:center;font-size:30px;line-height:37px;font-weight:500}

.features{left:0;top:1551px;width:1200px;height:1102px;background:linear-gradient(180deg,var(--pale),#dfeaf7)}
.card{width:534px;height:319px;background:var(--white);border-radius:8px;text-align:center;box-shadow:0 6px 20px rgba(20,50,110,.06)}
.badge{left:180px;top:-98px;width:174px;height:174px;border-radius:50%;background:var(--white);display:flex;align-items:center;justify-content:center}
.badge .dot{width:160px;height:160px;border-radius:50%;display:flex;align-items:center;justify-content:center}
.dot.light{background:linear-gradient(180deg,#3bb0f3,#1a86e0)}
.dot.dark{background:linear-gradient(180deg,#17377f,#0b1c52)}
.card h3{position:absolute;left:0;width:100%;top:126px;font-size:33px;font-weight:600}
.card p{position:absolute;left:60px;width:414px;top:186px;font-size:23px;line-height:31px;color:var(--muted)}

.review{left:138px;top:2819px;width:924px;height:325px;background:var(--white);border-radius:18px;box-shadow:0 4px 24px rgba(20,40,90,.12)}
.review p{position:absolute;left:40px;width:844px;top:52px;text-align:center;font-size:23px;line-height:34px;color:var(--ink)}
.review .who{position:absolute;left:0;width:100%;top:182px;text-align:center;font-size:31px;font-weight:600;color:var(--name)}
.review .stars{position:absolute;left:0;width:100%;top:240px;display:flex;justify-content:center;gap:4px}
.review .qmark{position:absolute;left:735px;top:168px}

.footer{left:0;top:3222px;width:1200px;height:240px;background:var(--navy-footer)}
.footer .brand{position:absolute;left:405px;top:58px}
.copy{left:0;width:1200px;top:3380px;text-align:center;color:var(--white);font-size:23px}
</style>
</head>
<body>

<header class="header abs">
  <div class="brand abs"><span class="brand-mark"></span>WebQuilt</div>
  <div class="social abs"><span></span><span></span><span></span><span></span><span></span></div>
</header>

<section class="hero abs">
  <div class="hero-art abs" role="img" aria-label="Illustration of an AI robot working on a glowing laptop surrounded by website layout previews"></div>
  <h1 class="hero-copy abs"><b>Artificial<br>Intelligence</b><br>to instantly<br>build stunning<br>websites<br><b>absolutely</b> <span class="free">FREE!</span></h1>
  <div class="btn abs">Try to create Now!</div>
</section>

<div class="eyebrow abs">Ai website Generator</div>
<h2 class="title abs" style="top:936px">Build a website <b>with AI</b></h2>

<div class="step-line abs" style="left:330px;width:132px"></div>
<div class="step-line abs" style="left:746px;width:124px"></div>

<div class="step abs" style="left:46px"><div class="core">
  <svg width="150" height="150" viewBox="0 0 150 150" fill="none" stroke="#fff" stroke-width="5"><rect x="10" y="14" width="130" height="90" rx="6"/><path d="M60 104v20M90 104v20M45 130h60"/><rect x="22" y="26" width="70" height="10" fill="#fff"/><rect x="24" y="48" width="10" height="10"/><rect x="24" y="66" width="10" height="10"/><rect x="24" y="84" width="10" height="10"/><path d="M42 53h40M42 71h30M42 89h36"/><path d="M98 58l28 12-12 4-4 12z"/></svg>
</div></div>
<div class="step abs" style="left:462px"><div class="core">
  <svg width="150" height="150" viewBox="0 0 150 150" fill="none" stroke="#fff" stroke-width="5"><rect x="10" y="14" width="130" height="90" rx="6"/><path d="M60 104v20M90 104v20M45 130h60"/><rect x="38" y="34" width="60" height="46"/><path d="M38 46h60"/><rect x="48" y="56" width="22" height="10"/><path d="M90 62l26 10-11 4-4 11z"/></svg>
</div></div>
<div class="step abs" style="left:870px"><div class="core">
  <svg width="150" height="150" viewBox="0 0 150 150" fill="none" stroke="#fff" stroke-width="5"><rect x="10" y="26" width="130" height="86" rx="6"/><path d="M10 96h130M75 112v14M50 132h50"/><rect x="34" y="10" width="82" height="86" fill="#1a86e0"/><path d="M44 26h20M70 26h36"/><rect x="44" y="40" width="30" height="26"/><path d="M82 44h24M82 54h24M82 64h24M44 78h62M44 86h62"/></svg>
</div></div>

<div class="step-label abs" style="left:28px">Enter your<br>Business<br>Name</div>
<div class="step-label abs" style="left:444px">Select<br>business category<br>(industry)</div>
<div class="step-label abs" style="left:852px">Create their<br>stunning new<br>website</div>

<section class="features abs" role="presentation"></section>
<h2 class="title abs" style="top:1604px">How you create website <b>with AI</b></h2>

<div class="card abs" style="left:46px;top:1802px">
  <div class="badge abs"><div class="dot light">
    <svg width="80" height="80" viewBox="0 0 80 80" fill="none" stroke="#fff" stroke-width="3.5"><rect x="26" y="8" width="30" height="54" rx="5"/><path d="M36 14h10"/><path d="M20 46c-4 6 0 14 8 20"/><circle cx="40" cy="40" r="30" stroke-dasharray="2 5"/></svg>
  </div></div>
  <h3>Mobile Focused</h3>
  <p>Your site will fit perfectly into a phone or tablet!</p>
</div>

<div class="card abs" style="left:618px;top:1802px">
  <div class="badge abs"><div class="dot dark">
    <svg width="80" height="80" viewBox="0 0 80 80" fill="none" stroke="#fff" stroke-width="3.5"><rect x="20" y="14" width="48" height="40" rx="3"/><path d="M12 26v34h44"/><circle cx="34" cy="26" r="5"/><path d="M22 50l14-14 10 10 8-8 14 12"/></svg>
  </div></div>
  <h3>Flexible Use</h3>
  <p>Customize your page with an image, video, animation, or anything else!</p>
</div>

<div class="card abs" style="left:46px;top:2247px">
  <div class="badge abs"><div class="dot light">
    <svg width="96" height="96" viewBox="0 0 96 96" fill="none" stroke="#fff" stroke-width="3.5"><circle cx="48" cy="48" r="40"/><circle cx="48" cy="48" r="33" stroke-width="2"/><text x="48" y="56" text-anchor="middle" fill="#fff" stroke="none" font-family="Poppins, sans-serif" font-weight="700" font-size="22">FREE</text></svg>
  </div></div>
  <h3>Free to Try</h3>
  <p>Get your site how you like it with a small monthly fee after.</p>
</div>

<div class="card abs" style="left:618px;top:2247px">
  <div class="badge abs"><div class="dot dark">
    <svg width="84" height="84" viewBox="0 0 84 84" fill="none" stroke="#fff" stroke-width="3"><path d="M22 48a12 12 0 010-24 18 18 0 0134-4 12 12 0 016 28z"/><rect x="30" y="28" width="24" height="24"/><path d="M30 36h24M30 44h24M42 52v10M32 52v8l-6 6M52 52v8l6 6"/><circle cx="42" cy="66" r="3"/><circle cx="24" cy="68" r="3"/><circle cx="60" cy="68" r="3"/></svg>
  </div></div>
  <h3>Cloud Strength</h3>
  <p style="left:40px;width:454px">All sites run in a secure, high-powered cloud computing environment!</p>
</div>

<h2 class="title abs" style="top:2712px">What our site <b>owner says</b></h2>
<div class="review abs">
  <p>“ Lorem Ipsum is simply dummy text of the printing and typesetting industry. Lorem Ipsum has been the industry's standard dummy text ever since the 1500s, when an unknown printer took a galley”</p>
  <div class="who">Nora Whitfield</div>
  <div class="stars">
    <svg width="150" height="28" viewBox="0 0 150 28" fill="var(--star)"><g id="s"><path d="M14 1l4 9 9 1-7 6 2 9-8-5-8 5 2-9-7-6 9-1z"/></g><use href="#s" x="30"/><use href="#s" x="60"/><use href="#s" x="90"/><use href="#s" x="120"/></svg>
  </div>
  <svg class="qmark" width="134" height="110" viewBox="0 0 134 110" fill="var(--quote)"><path d="M4 110V62C4 26 22 6 56 0l4 14C40 20 32 32 32 50h26v60zM76 110V62c0-36 18-56 52-62l4 14c-20 6-28 18-28 36h26v60z"/></svg>
</div>

<footer class="footer abs">
  <div class="brand"><span class="brand-mark"></span>WebQuilt</div>
</footer>
<div class="copy abs">Copyright © 2023 WebQuilt &nbsp;| All Right Reserved</div>

</body>
</html>
```